Web Design for Financial Consulting Company

We need a website design for a financial consulting company "Kelvane Consulting". We build financial models, scenario analysis, handle the budgeting process and provide temporary staffing. I have over 10 years of experience. My Excel expertise and analytical savvy has saved clients over $17 million in profit.

Target Market(s)

Small to medium businesses

Industry/Entity Type

Financial Consulting

Number of Pages Required

4 page

Requirements
Must have
• Professional looking
Nice to have
• A little futuristic looking

```html
<!DOCTYPE html>
<html lang="en">
<head>
<meta charset="utf-8">
<title>Kelvane Consulting</title>
<link href="https://fonts.googleapis.com/css2?family=Varela+Round&family=Montserrat:wght@400;500;600&display=swap" rel="stylesheet">
<style>
:root{
  --night:#050a2c;
  --sky:#00a8f0;
  --navy:#033d69;
  --ink:#0a3457;
  --text:#3a3a3a;
  --card:#f5f5f5;
  --star:#f7a400;
  --white:#ffffff;
}
*{margin:0;padding:0;box-sizing:border-box}
html,body{width:1200px;height:2638px;overflow:hidden;background:var(--white)}
body{position:relative;font-family:"Varela Round",sans-serif;color:var(--text)}
.abs{position:absolute}
.shapes{position:absolute;left:0;top:0}
.brand{display:flex;align-items:center;gap:12px;color:var(--white);font-family:"Varela Round",sans-serif;font-size:30px;letter-spacing:1px;white-space:nowrap}
.brand-square{width:34px;height:34px;background:var(--sky)}
.nav{display:flex;align-items:center;font-family:"Montserrat",sans-serif;font-weight:500;font-size:15px;color:var(--white)}
.nav a{color:inherit;text-decoration:none}
.nav-top{left:690px;top:22px;gap:0}
.nav-top a{padding:0 25px;line-height:48px}
.nav-top a.cta{background:var(--sky);color:var(--ink);padding:0 20px;margin-left:-6px}
.hero-title{left:99px;top:196px;width:560px;font-size:50px;line-height:66px;color:var(--white)}
.btn{display:inline-block;background:var(--sky);color:var(--ink);font-size:16px;line-height:48px;padding:0 14px;font-family:"Varela Round",sans-serif}
.hero-btn{left:98px;top:414px;width:120px;text-align:center}
.hero-visual{left:680px;top:90px;width:430px;height:430px;border-radius:50%;background:radial-gradient(circle at 60% 45%,rgba(60,200,255,.55),rgba(20,90,200,.25) 45%,rgba(5,10,44,0) 70%)}
.about-visual{left:96px;top:673px;width:417px;height:419px;background:linear-gradient(145deg,#1f5f86,#173e5c 45%,#0e2a42 70%,#2a6f9a)}
.eyebrow{font-size:21px;color:var(--ink)}
.big{font-size:37px;letter-spacing:1px;color:var(--ink)}
.big span{color:var(--sky)}
.about-text{left:546px;top:733px;width:550px}
.about-text p{font-size:15px;line-height:28px;color:#333;margin-top:4px}
.about-text p.lead{color:var(--sky);font-size:17px;line-height:29px;margin-top:8px}
.center{left:0;width:1200px;text-align:center}
.cards{left:97px;top:1285px;display:flex;gap:13px}
.card{width:190px;height:242px;background:var(--card);border-right:1px solid #bcd6ea;border-bottom:1px solid #bcd6ea;position:relative}
.card.active{background:var(--navy)}
.card svg{position:absolute;left:10px;top:48px}
.card h3{position:absolute;left:11px;top:148px;font-family:"Montserrat",sans-serif;font-weight:500;font-size:17px;line-height:23px;color:#333}
.card.active h3{color:var(--white)}
.call-btn{left:390px;top:1562px;width:393px;height:65px;background:var(--navy);color:var(--white);display:flex;align-items:center;gap:14px;padding-left:20px;font-size:19px;letter-spacing:.5px}
.review{width:484px;height:243px;background:var(--white);box-shadow:0 2px 14px rgba(0,0,0,.07);top:1815px;padding:20px 16px}
.review p{font-size:15px;line-height:28px;color:#333}
.review .who{font-family:"Montserrat",sans-serif;font-weight:500;font-size:16px;color:var(--ink);margin:22px 0 0 8px}
.stars{margin:6px 0 0 8px;color:var(--star);font-size:15px;letter-spacing:2px}
.quote{position:absolute;right:30px;top:118px;font-family:Georgia,serif;font-size:160px;line-height:1;color:#ececec}
.dots{left:496px;top:2123px;display:flex;gap:12px}
.dots i{width:30px;height:4px;background:var(--sky);display:block}
.dots i.on{background:var(--navy)}
.foot-brand{left:0;width:1200px;top:2312px;justify-content:center}
.nav-foot{left:0;width:1200px;top:2386px;justify-content:center;gap:52px}
.rule{left:94px;width:1004px;height:1px;background:rgba(255,255,255,.18)}
.contact{display:flex;align-items:center;gap:10px;color:var(--white);font-family:"Montserrat",sans-serif;font-size:14px;line-height:20px}
.contact .tile{width:52px;height:52px;background:var(--sky);display:flex;align-items:center;justify-content:center}
.contact b{font-weight:500;font-size:16px;display:block}
.copy{left:0;width:1200px;top:2584px;text-align:center;color:var(--white);font-family:"Montserrat",sans-serif;font-size:14px}
</style>
</head>
<body>
<svg class="shapes" width="1200" height="2638" aria-hidden="true">
  <polygon points="0,0 1200,0 1200,508 0,600" fill="#050a2c"/>
  <line x1="0" y1="600" x2="1200" y2="508" stroke="#00a8f0" stroke-width="5"/>
  <polygon points="0,2287 1200,2190 1200,2638 0,2638" fill="#033d69"/>
  <line x1="0" y1="2287" x2="1200" y2="2190" stroke="#00a8f0" stroke-width="5"/>
</svg>

<header>
  <div class="abs brand" style="left:97px;top:30px"><span class="brand-square"></span>Kelvane Consulting</div>
  <nav class="abs nav nav-top"><a href="#">Home</a><a href="#">About Us</a><a href="#">Services</a><a href="#" class="cta">Contact Us</a></nav>
</header>

<section>
  <h1 class="abs hero-title" style="font-weight:400">Helping Your Finance Team And Increasing Profit</h1>
  <a class="abs btn hero-btn" href="#">Contact Us</a>
  <div class="abs hero-visual" role="img" aria-label="Glowing blue candlestick chart rising over a dotted world map"></div>
</section>

<section>
  <div class="abs about-visual" role="img" aria-label="Businessman's hand drawing a rising white growth arrow over bar graphs"></div>
  <div class="abs about-text">
    <div class="eyebrow">About</div>
    <h2 class="big" style="font-weight:400">KELVANE <span>CONSULTING</span></h2>
    <p>Lorem ipsum dolor sit amet, consectetuer adipiscing elit, sed diam nonummy nibh euismod tincidunt ut laoreet dolore magna aliquam erat volutpat. Ut wisi enim ad minim veniam, quis nostrud exerci tation ullamcorper suscipit lobortis nisl.</p>
    <p>Our courteous, professional team is able to support a range of services to meet your requirements.</p>
    <p class="lead">To Learn More About Kelvane Consulting Services, Please Call Us At 555.014.2290</p>
  </div>
</section>

<section>
  <div class="abs center" style="top:1187px">
    <div class="eyebrow">What We Offer</div>
    <h2 class="big" style="font-weight:400">OUR <span>SERVICES</span></h2>
  </div>
  <div class="abs cards">
    <div class="card">
      <svg width="80" height="80" viewBox="0 0 80 80" fill="none" stroke="#0a3457" stroke-width="2.5"><rect x="2" y="34" width="18" height="14"/><rect x="50" y="20" width="24" height="16"/><rect x="50" y="46" width="24" height="16"/><path d="M36 10v52M20 41h16M36 28h14M36 54h14"/><circle cx="36" cy="8" r="5" stroke="#00a8f0"/></svg>
      <h3>Financial Models Projects</h3>
    </div>
    <div class="card active">
      <svg width="80" height="80" viewBox="0 0 80 80" fill="none" stroke="#fff" stroke-width="2.5"><circle cx="40" cy="18" r="14" stroke="#00a8f0"/><path d="M40 32v14M12 46h56M12 46v12M68 46v12M40 46v12"/><rect x="4" y="58" width="16" height="14"/><rect x="32" y="58" width="16" height="14"/><rect x="60" y="58" width="16" height="14"/><text x="35" y="24" fill="#00a8f0" stroke="none" font-size="16" font-family="sans-serif">$</text></svg>
      <h3>Budgeting Process</h3>
    </div>
    <div class="card">
      <svg width="80" height="80" viewBox="0 0 80 80" fill="none" stroke="#0a3457" stroke-width="3"><circle cx="20" cy="12" r="6" stroke="#00a8f0"/><circle cx="40" cy="12" r="6" stroke="#00a8f0"/><circle cx="60" cy="12" r="6" stroke="#00a8f0"/><circle cx="40" cy="48" r="22"/><circle cx="40" cy="48" r="10"/><path d="M10 40q10-14 20 0q10-14 20 0q10-14 20 0"/></svg>
      <h3>Temporary Staffing</h3>
    </div>
    <div class="card">
      <svg width="80" height="80" viewBox="0 0 80 80" fill="none" stroke="#0a3457" stroke-width="2.5"><ellipse cx="34" cy="10" rx="30" ry="7"/><path d="M4 10v58c0 4 14 7 30 7s30-3 30-7V10M4 30c0 4 14 7 30 7s30-3 30-7M4 50c0 4 14 7 30 7"/><path d="M36 40l4-12M30 56l6-16h8l6 16z" stroke="#00a8f0"/></svg>
      <h3>Data Cleansing</h3>
    </div>
    <div class="card">
      <svg width="80" height="80" viewBox="0 0 80 80" fill="none" stroke="#0a3457" stroke-width="2.5"><circle cx="40" cy="40" r="32"/><circle cx="40" cy="8" r="5"/><circle cx="8" cy="40" r="5"/><circle cx="72" cy="40" r="5"/><path d="M28 54V42l-5 4M40 54V34l-5 5M40 34l5 5M52 54V40l5 5" stroke="#00a8f0"/></svg>
      <h3>Process Improvement</h3>
    </div>
  </div>
  <a class="abs call-btn" href="#">
    <svg width="30" height="30" viewBox="0 0 30 30" fill="none" stroke="#fff" stroke-width="1.8"><path d="M6 3l5 6-3 3c2 4 5 7 9 9l3-3 6 5-3 4C12 26 4 18 2 6z"/><path d="M17 3a10 10 0 0 1 10 10M17 8a5 5 0 0 1 5 5"/></svg>
    Contact Us Today 555.014.2290
  </a>
</section>

<section>
  <div class="abs center" style="top:1723px">
    <div class="eyebrow">Results</div>
    <h2 class="big" style="font-weight:400">HAPPY CUSTOMER <span>REVIEWS</span></h2>
  </div>
  <article class="abs review" style="left:97px">
    <p>Lorem ipsum dolor sit amet, consectetuer adipiscing elit, sed diam nonummy nibh euismod tincidunt ut laoreet dolore magna aliquam erat volutpat. Ut wisi enici tation ullamcorper suscipit lobortis nisl.</p>
    <div class="who">Marla T.</div>
    <div class="stars">★★★★★</div>
    <span class="quote">”</span>
  </article>
  <article class="abs review" style="left:615px">
    <p>Lorem ipsum dolor sit amet, consectetuer adipiscing elit, sed diam nonummy nibh euismod tincidunt ut laoreet dolore magna aliquam erat volutpat. Ut wisi enici tation ullamcorper suscipit lobortis nisl.</p>
    <div class="who">Renata V.</div>
    <div class="stars">★★★★★</div>
    <span class="quote">”</span>
  </article>
  <div class="abs dots"><i></i><i></i><i class="on"></i><i></i><i></i></div>
</section>

<footer>
  <div class="abs brand foot-brand"><span class="brand-square"></span>Kelvane Consulting</div>
  <nav class="abs nav nav-foot"><a href="#">Home</a><a href="#">About Us</a><a href="#">Services</a><a href="#">Contact Us</a></nav>
  <div class="abs rule" style="top:2437px"></div>
  <div class="abs contact" style="left:112px;top:2472px">
    <span class="tile"><svg width="26" height="26" viewBox="0 0 30 30" fill="none" stroke="#fff" stroke-width="1.8"><path d="M6 3l5 6-3 3c2 4 5 7 9 9l3-3 6 5-3 4C12 26 4 18 2 6z"/></svg></span>
    <div><b>Phone</b>555.014.2290</div>
  </div>
  <div class="abs contact" style="left:397px;top:2472px">
    <span class="tile"><svg width="24" height="28" viewBox="0 0 24 28" fill="none" stroke="#fff" stroke-width="1.8"><path d="M12 27C4 17 2 13 2 10a10 10 0 0 1 20 0c0 3-2 7-10 17z"/><circle cx="12" cy="10" r="4"/></svg></span>
    <div>123 Ipsum Dolor Sit Am Constuer<br>Adipiscing Elit Sed Diam.</div>
  </div>
  <div class="abs contact" style="left:818px;top:2472px">
    <span class="tile"><svg width="30" height="26" viewBox="0 0 30 26" fill="none" stroke="#fff" stroke-width="1.8"><rect x="2" y="6" width="26" height="18"/><path d="M2 6l13 10 13-10M2 24l10-9M28 24l-10-9"/></svg></span>
    <div><b>Email</b>info@kelvaneconsulting.com</div>
  </div>
  <div class="abs rule" style="top:2557px"></div>
  <div class="abs copy">© 2023 Kelvane Consulting. All Rights Reserved.</div>
</footer>
</body>
</html>
```